Cosmetic retail chain developes private label products. We need package designe for creme soap.

We need package designe for bar creme soap in cardboard package. Benchmark is Tulk. The name of our private label for this product is Nerisa.

```html
<!DOCTYPE html>
<html lang="en">
<head>
<meta charset="utf-8">
<title>Nerisa Cream Soap – Package</title>
<link rel="stylesheet" href="https://fonts.googleapis.com/css2?family=Montserrat:wght@400;500&display=swap">
<style>
  :root {
    --backdrop: #e9ebed;
    --lid: #f3f4f5;
    --lid-shade: #dfe1e3;
    --gold: #a98b45;
    --gold-light: #c9ad6a;
    --blue: #1d4fa6;
    --white: #ffffff;
  }
  * { margin: 0; padding: 0; box-sizing: border-box; }
  html, body { width: 1200px; height: 789px; overflow: hidden; background: var(--backdrop); }
  .canvas {
    position: relative; width: 1200px; height: 789px;
    display: flex; align-items: center; justify-content: center;
  }
  .package { display: flex; flex-direction: column; width: 640px; }
  .lid {
    position: relative; height: 440px;
    background: linear-gradient(160deg, var(--lid) 0%, var(--lid) 55%, var(--lid-shade) 100%);
  }
  .splash {
    position: absolute; right: 0; bottom: 0; width: 62%; height: 70%;
    background: radial-gradient(ellipse at 70% 75%, #ffffff 0%, #eef0f1 45%, rgba(243,244,245,0) 75%);
  }
  .brand-name {
    position: absolute; left: 50%; top: 50%;
    transform: translate(-50%, -50%);
    font-family: "Montserrat", sans-serif; font-weight: 400;
    font-size: 64px; color: var(--gold); letter-spacing: 2px;
    white-space: nowrap;
  }
  .side {
    position: relative; height: 120px; background: var(--blue);
    border-top: 10px solid var(--gold);
    display: flex; align-items: center; justify-content: space-between;
    padding: 0 40px;
  }
  .side-claim, .side-name {
    font-family: "Montserrat", sans-serif; font-weight: 500;
    font-size: 17px; letter-spacing: 1.5px; text-transform: uppercase;
  }
  .side-claim { color: var(--white); }
  .side-name { color: var(--gold-light); font-weight: 400; font-size: 24px; text-transform: none; letter-spacing: 1px; }
</style>
</head>
<body>
  <main class="canvas">
    <section class="package">
      <div class="lid">
        <div class="splash" role="img" aria-label="Splash of milky cream across the lid"></div>
        <span class="brand-name">Nerisa</span>
      </div>
      <div class="side">
        <span class="side-claim">100% Natural Cream Soap</span>
        <span class="side-name">Nerisa</span>
      </div>
    </section>
  </main>
</body>
</html>
```